Brisk Treadway - Design Australia's largest Tyre ecommerce website!

We need a home page design and headers for the other pages.

Our site is built on magento community and is up and running at
brisktreadway.com.au
so you can see what we do. Basically all the elements on the current home page are required but don't have to stay in the current form. This is just a template we used to get the site functional with little regard to design.

We are the only tyre company in Australia that is 100% online. We sell tyres for almost every vehicle including motor bikes, cars, 4x4, trucks tractors, ATVs mining equipment. We have no shopfront, we dont fit tyres or run a shopfront. We just sell and ship tyres at the best prices possible.

We want a design that
* uses complimentary colours to our logo.
* has space for the video and tyre chooser - without scrolling the tyre chooser needs to be visible at least in part. The chooser is a key element. This is how most customers will find their tyre.
* in the header or somewhere prominent on the homepage we want to advertise
Australia Wide Delivery
Free delivery to Brisbane Sydney Melbourne
$20 to all other locations **with few exceptions (the small print)
Fast Delivery to your door -
1-3 Business days to most metro areas
5-10 Business days to all other areas **With few exceptions

On the home page we also want
* links to our facebook and twitter accounts
* a specials banner/space, with space to display up to 20 items.
* customer testimonials space

Thanks in advance!
Updates

Hi - It is in the job description but just to emphasise, the tyre chooser and intro video are key elements of our page and we need users to be drawn to them in a very visual way. Not flashing neon lights but some kind of elegant clean design. 

There are two paths a user may take - most will go straight to the tyre chooser to find their product. The rest will click on a category and then use the "shop by" filters to quickly refine their search.

Target Market(s)

18-30 Male retail. Truck and heavy equipment companies

Industry/Entity Type

Business

Requirements
Must have
• We want a design that
Australia Wide Delivery
Nice to have
• Possibly a graphic that indicates that we sell all tyres and not just cars and 4x4

```html
<!DOCTYPE html>
<html lang="en">
<head>
<meta charset="utf-8">
<title>Brisk Treadway – Your Online Tyre Company</title>
<link rel="stylesheet" href="https://fonts.googleapis.com/css2?family=Ropa+Sans&family=Roboto:wght@300;400;500;700&family=Roboto+Condensed:wght@400;700&display=swap">
<style>
:root{
  --page-bg:#eeeeee;
  --white:#ffffff;
  --ink:#222222;
  --muted:#a8a8a8;
  --nav-grey:#9a9a9a;
  --red:#c4161c;
  --red-dark:#9d0d12;
  --blue-light:#0aa6e6;
  --blue-deep:#1d3f9d;
  --chooser-blue:#0b6fc0;
  --delivery-blue:#1b468c;
  --footer:#353535;
  --footer-bottom:#242424;
  --footer-text:#c9c9c9;
  --rule:#cfcfcf;
}
*{box-sizing:border-box;margin:0;padding:0}
html,body{width:1067px;height:1200px;overflow:hidden;background:var(--page-bg);font-family:"Roboto",Arial,sans-serif;color:var(--ink)}
.page{position:absolute;left:98px;top:0;width:871px;height:949px;background:var(--white);box-shadow:0 0 4px rgba(0,0,0,.15)}
.abs{position:absolute}

/* header */
.brand{left:9px;top:28px;display:flex;align-items:center;gap:8px;font-family:"Ropa Sans",sans-serif;font-size:27px;color:var(--red);letter-spacing:.5px}
.brand-square{width:18px;height:18px;background:var(--blue-deep)}
.search{left:364px;top:49px;width:219px;height:27px;border:1px solid #d6d6d6;font-size:10px;color:#b5b5b5;display:flex;align-items:center;justify-content:space-between;padding:0 8px}
.cart{right:8px;top:24px;font-size:11px;color:#b0b0b0;font-weight:300;display:flex;align-items:center;gap:5px}
.cart b{color:var(--ink);font-weight:400}
.cart-bag{width:10px;height:9px;background:#333;border-radius:1px}
.account-links{right:8px;top:61px;font-size:11.5px;color:var(--ink);display:flex;gap:10px;font-family:"Roboto Condensed",sans-serif}
.account-links span.sep{color:#777}

.main-nav{left:9px;top:100px;width:853px;height:33px;border-bottom:4px double #a5a5a5}
.main-nav ul{list-style:none;display:flex;padding-left:17px;font-family:"Roboto Condensed",sans-serif;font-size:13.5px;color:var(--nav-grey)}
.main-nav li{height:29px;line-height:29px;padding:0 14.5px}
.main-nav li.active{color:var(--red);border:1px solid #c5c5c5;border-bottom:none;background:var(--white)}

/* hero */
.hero{left:9px;top:140px;width:853px;height:320px;background:linear-gradient(100deg,var(--blue-light) 0%,#0a8ad6 45%,var(--blue-deep) 100%)}
.hero-video{left:18px;top:45px;width:393px;height:229px;border:1px solid #e8e8e8;background:linear-gradient(120deg,#6f6a66,#2b2b2b 70%,#1a1a1a)}
.play{left:50%;top:50%;transform:translate(-50%,-50%)}
.hero-dots{left:18px;top:297px;display:flex;gap:9px}
.hero-dots i{width:12px;height:12px;border:1.5px solid var(--white);display:block}
.hero-dots i.on{background:var(--red)}
.hero-graphic{left:450px;top:40px;width:403px;height:280px;background:linear-gradient(160deg,rgba(20,60,150,.35) 0%,rgba(60,70,90,.55) 100%)}

/* welcome */
.welcome{left:9px;top:487px;width:555px}
.welcome h1{font-family:"Ropa Sans",sans-serif;font-weight:400;font-size:24px;color:#111;margin-bottom:11px}
.welcome p{font-size:11px;line-height:16px;color:var(--muted);font-weight:300;margin-bottom:7px}
.btn-red{display:inline-block;background:var(--red);color:var(--white);font-size:11.5px;padding:6px 6px;margin-top:6px;border:1px solid var(--red-dark)}

.delivery{left:9px;top:660px;width:555px;height:147px;background:linear-gradient(90deg,var(--delivery-blue),#1f4f99 70%,#2a5fab);color:var(--white);box-shadow:0 8px 7px -6px rgba(0,0,0,.45)}
.delivery .copy{position:absolute;left:15px;top:8px;width:305px}
.delivery h2{font-family:"Roboto Condensed",sans-serif;font-weight:700;font-size:23px;line-height:28px}
.delivery h3{font-family:"Roboto Condensed",sans-serif;font-weight:400;font-size:19px;margin-top:8px}
.delivery p{font-size:10.5px;line-height:18px;margin-top:6px}
.delivery .truck{position:absolute;left:385px;top:20px}
.delivery .aus{position:absolute;left:344px;top:106px;width:205px;text-align:center;font-weight:700;font-size:16.5px;font-family:"Roboto",sans-serif}

/* chooser */
.chooser{left:594px;top:486px;width:269px;height:330px;background:var(--chooser-blue);border:1px solid #08519a;border-top:3px solid var(--red);color:var(--white);padding:10px 12px}
.chooser h2{font-family:"Ropa Sans",sans-serif;font-weight:400;font-size:24px;line-height:26px}
.chooser .lead{font-family:"Ropa Sans",sans-serif;font-size:15px;line-height:22px;margin-top:2px}
.fields{display:grid;grid-template-columns:110px 110px;column-gap:11px;row-gap:8px;margin-top:8px;padding-left:1px}
.field label{display:block;font-family:"Ropa Sans",sans-serif;font-size:12.5px;margin:0 0 5px 2px}
.field .box{height:27px;background:var(--white);position:relative}
.field .box::after{content:"";position:absolute;right:0;top:0;border-style:solid;border-width:0 14px 14px 0;border-color:transparent #17a6d8 transparent transparent}
.btn-find{display:block;margin:24px auto 0;width:145px;height:34px;background:linear-gradient(#d21a20,#a50d12);color:var(--white);text-align:center;line-height:34px;font-family:"Roboto Condensed",sans-serif;font-weight:700;font-size:14px;border-radius:2px}

/* partners */
.partners-title{left:9px;top:840px;width:853px;text-align:center}
.partners-title::before{content:"";position:absolute;left:0;right:0;top:12px;border-top:1px solid var(--rule)}
.partners-title span{position:relative;background:var(--white);padding:0 8px;font-family:"Ropa Sans",sans-serif;font-size:19px;color:#555}
.partners{left:9px;top:879px;width:853px;display:flex;justify-content:space-around;align-items:center}
.partner{display:block}

/* footer */
.footer{position:absolute;left:0;top:949px;width:1067px;height:202px;background:var(--footer)}
.fcol{position:absolute;top:27px}
.fcol h4{font-family:"Roboto",sans-serif;font-weight:500;font-size:15.5px;color:var(--white);height:28px;border-bottom:1px solid #555;width:123px;margin-bottom:9px}
.fcol ul{list-style:none;font-size:11.5px;color:var(--footer-text);padding-left:2px}
.fcol li{height:20px}
.bottom-bar{position:absolute;left:0;top:1151px;width:1067px;height:49px;background:var(--footer-bottom);color:var(--footer-text);font-size:11.5px}
.bottom-bar .copy{position:absolute;left:111px;top:16px}
.bottom-bar .legal{position:absolute;right:109px;top:16px;display:flex;gap:10px}
</style>
</head>
<body>
<div class="page">
  <header>
    <div class="abs brand"><span class="brand-square"></span>BRISK TREADWAY</div>
    <div class="abs search"><span>Search tyres...</span><span>GO</span></div>
    <div class="abs cart">Shopping Cart - <b>$0.00</b><span class="cart-bag"></span></div>
    <nav class="abs account-links"><span>My Account</span><span class="sep">|</span><span>My Wishlist</span><span class="sep">|</span><span>Checkout</span><span class="sep">|</span><span>Log in</span></nav>
    <nav class="abs main-nav">
      <ul>
        <li class="active">HOME</li><li>CAR</li><li>4X4</li><li>LIGHT TRUCK</li><li>TRUCK</li><li>AGRICULTURE/OTR</li><li>MOTORBIKE</li><li>TRAILER/CARAVAN</li><li>RIMS</li><li>TUBES</li>
      </ul>
    </nav>
  </header>

  <section class="abs hero">
    <div class="abs hero-video" role="img" aria-label="Intro video still of a mechanic fitting a wheel">
      <svg class="abs play" width="36" height="40" viewBox="0 0 36 40"><path d="M2 2 L34 20 L2 38 Z" fill="rgba(255,255,255,.55)"/></svg>
    </div>
    <div class="abs hero-dots"><i></i><i></i><i></i><i class="on"></i></div>
    <div class="abs hero-graphic" role="img" aria-label="Illustration explaining tyre sidewall markings for width, profile, size and speed"></div>
  </section>

  <section class="abs welcome">
    <h1>WELCOME TO OUR SITE</h1>
    <p>Sed ut perspiciatis unde omnis iste natus error sit voluptatem accusantium doloremque laudantium, totam rem aperiam, eaque ipsa quae ab illo inventore veritatis et quasi architecto beatae vitae dicta sunt explicabo. Nemo enim ipsam voluptatem quia voluptas sit aspernatur aut odit aut fugit.</p>
    <p>Sed quia consequuntur magni dolores eos qui ratione voluptatem sequi nesciunt beatae vitae dicta sunt explicabo...</p>
    <span class="btn-red">Read More</span>
  </section>

  <section class="abs delivery">
    <div class="copy">
      <h2>Free Delivery To<br>“Brisbane Sydney Melbourne”</h2>
      <h3>$20 to all other locations</h3>
      <p>Fast Delivery to your door 1-3 Business days to most metro areas 5-10 Business days to all other areas</p>
    </div>
    <svg class="truck" width="112" height="72" viewBox="0 0 112 72">
      <rect x="0" y="14" width="36" height="40" rx="5" fill="#fff"/>
      <rect x="6" y="20" width="18" height="14" fill="#1b468c"/>
      <rect x="40" y="0" width="72" height="54" rx="3" fill="#fff"/>
      <circle cx="18" cy="60" r="10" fill="#fff" stroke="#1b468c" stroke-width="3"/>
      <circle cx="66" cy="60" r="10" fill="#fff" stroke="#1b468c" stroke-width="3"/>
      <circle cx="92" cy="60" r="10" fill="#fff" stroke="#1b468c" stroke-width="3"/>
    </svg>
    <div class="aus">Australia Wide Delivery</div>
  </section>

  <aside class="abs chooser">
    <h2>TYRE CHOOSER</h2>
    <p class="lead">Please select from the boxes to find your Tyres.</p>
    <div class="fields">
      <div class="field"><label>Width</label><div class="box"></div></div>
      <div class="field"><label>Profile Or Height</label><div class="box"></div></div>
      <div class="field"><label>Rim</label><div class="box"></div></div>
      <div class="field"><label>Brand</label><div class="box"></div></div>
      <div class="field"><label>Vehcile</label><div class="box"></div></div>
      <div class="field"><label>Accessories</label><div class="box"></div></div>
    </div>
    <span class="btn-find">GFIND MY TYRES</span>
  </aside>

  <div class="abs partners-title"><span>Our Partners</span></div>
  <div class="abs partners">
    <svg class="partner" width="81" height="41" role="img" aria-label="Partner badge"><rect width="81" height="41" fill="#1e1e1e"/></svg>
    <svg class="partner" width="90" height="30" role="img" aria-label="Partner badge"><rect y="6" width="60" height="18" fill="#b9b9b9"/><circle cx="76" cy="15" r="14" fill="#333"/></svg>
    <svg class="partner" width="94" height="34" role="img" aria-label="Partner badge"><rect width="94" height="34" fill="#d8d8d8"/></svg>
    <svg class="partner" width="103" height="26" role="img" aria-label="Partner badge"><rect width="103" height="26" fill="#d42a26"/></svg>
    <svg class="partner" width="92" height="14" role="img" aria-label="Partner badge"><rect width="92" height="14" fill="#cfcfcf"/></svg>
  </div>
</div>

<footer class="footer">
  <div class="fcol" style="left:107px"><h4>Information</h4><ul><li>About Us</li><li>Customer Services</li><li>Privacy Policy</li><li>Site Map</li><li>Search Term</li></ul></div>
  <div class="fcol" style="left:259px"><h4>&nbsp;</h4><ul><li>Advanced Search</li><li>Orders and Returns</li><li>Contact Us</li></ul></div>
  <div class="fcol" style="left:442px"><h4>Why Buy From Us</h4><ul><li>Shipping &amp; Returns</li><li>Secure Shopping</li><li>Dolor Sit Amet</li><li>Consectetur</li><li>Adipisicing Elit</li></ul></div>
  <div class="fcol" style="left:637px"><h4 style="width:106px">My Account</h4><ul><li>Sign In</li><li>View Cart</li><li>My Wishlist</li></ul></div>
  <div class="fcol" style="left:787px"><h4>Brisk Treadway</h4><ul><li>No Risk Guarantee</li><li>High Rollers</li><li>FAQ</li></ul></div>
</footer>
<div class="bottom-bar">
  <span class="copy">Copyright © 2013 Brisk Treadway. All Rights Reserved.</span>
  <span class="legal"><span>Terms Of Use</span><span>|</span><span>Privacy Policy</span></span>
</div>
</body>
</html>
```